Brightwell Recovery Email Marketing Design

Dear Designer,
We're in need of an email background template for our company, Brightwell Recovery, that reflects our commitment to building lasting relationships with our clients and providing top-quality restoration and cleaning services.
We'd like the template to incorporate our brand colors, which are #F2F2F3, #005EA5, #468ECC, and #000000, and to feature images related to our services, such as water restoration, emergency flood response, mold remediation, trauma scene clean-up, fire restoration, carpet cleaning, and more. Our logo and tagline, "Calm Returns", should be prominently displayed in a unique and visually appealing way, along with our website address, www.brightwellrecovery.example.
The email should be professional and positive, highlighting the camaraderie and teamwork among our employees. We want to thank our clients for their business, offer a special discount, and promote our services. The final design should be visually stunning and memorable, with a clear call-to-action to encourage clients to take advantage of the discount.
We'd like the final design in JPG or PNG format, with a resolution of at least 720x720 pixels.
Thank you for considering this project. We're excited to see what you come up with!
Best regards,
Tavin

```html
<!DOCTYPE html>
<html lang="en">
<head>
<meta charset="utf-8">
<title>Brightwell Recovery – Calm Returns</title>
<link rel="stylesheet" href="https://fonts.googleapis.com/css2?family=Montserrat:wght@500;600;700&family=Playfair+Display:wght@700;800&display=swap">
<style>
  :root {
    --blue-deep: #1656a6;
    --blue-mid: #2a6fbe;
    --blue-light: #468ecc;
    --brand: #005ea5;
    --white: #ffffff;
    --off-white: #f2f2f3;
    --ink: #0b3f86;
  }
  * { margin: 0; padding: 0; box-sizing: border-box; }
  html, body { width: 1200px; height: 1200px; overflow: hidden; }
  body {
    background: linear-gradient(135deg, var(--blue-deep) 0%, var(--blue-mid) 60%, var(--blue-light) 100%);
    font-family: "Montserrat", sans-serif;
    color: var(--white);
    position: relative;
  }
  .backdrop { position: absolute; inset: 0; }
  .brand-name {
    position: absolute; left: 762px; top: 104px; width: 400px;
    text-align: center;
    font-family: "Playfair Display", serif; font-weight: 800;
    font-size: 34px; letter-spacing: 1px; color: var(--white);
    text-transform: uppercase;
  }
  .headline {
    position: absolute; left: 752px; top: 316px;
    font-family: "Playfair Display", serif; font-weight: 800;
    font-size: 66px; line-height: 82px; letter-spacing: 1px;
    text-transform: uppercase;
  }
  .rule { position: absolute; height: 4px; background: var(--blue-light); border-radius: 2px; }
  .rule--headline { left: 752px; top: 500px; width: 298px; }
  .rule--services { left: 752px; top: 779px; width: 184px; }
  .intro {
    position: absolute; left: 752px; top: 530px; width: 350px;
    font-size: 15.5px; line-height: 20px; font-weight: 500; color: var(--off-white);
  }
  .services-title {
    position: absolute; left: 752px; top: 734px;
    font-family: "Playfair Display", serif; font-weight: 700; font-size: 29px;
  }
  .service-list { position: absolute; left: 752px; top: 818px; list-style: none; }
  .service-list li {
    display: flex; align-items: center; gap: 16px;
    height: 37px; font-size: 18px; font-weight: 500; color: var(--off-white);
  }
  .service-list svg { width: 24px; height: 24px; flex: none; }
  .cta {
    position: absolute; left: 752px; top: 988px; width: 211px; height: 60px;
    border-radius: 30px; background: var(--white); color: var(--ink);
    display: flex; align-items: center; justify-content: center;
    font-weight: 700; font-size: 22px; letter-spacing: .5px; text-decoration: none;
  }
  .contact-phone { position: absolute; left: 80px; top: 1094px; display: flex; align-items: center; gap: 24px; }
  .contact-phone svg { width: 62px; height: 62px; }
  .contact-label { font-size: 18px; font-weight: 700; }
  .contact-number { font-size: 25px; font-weight: 700; margin-top: 4px; }
  .contact-web { position: absolute; left: 664px; top: 1108px; display: flex; align-items: center; gap: 14px; }
  .contact-web svg { width: 30px; height: 30px; }
  .contact-web span { font-size: 20.5px; font-weight: 700; }
</style>
</head>
<body>
  <svg class="backdrop" width="1200" height="1200" viewBox="0 0 1200 1200">
    <defs>
      <linearGradient id="photoTone" x1="0" y1="0" x2="1" y2="1">
        <stop offset="0" stop-color="#b5694f"/>
        <stop offset="0.45" stop-color="#d9d3cc"/>
        <stop offset="1" stop-color="#2d5fb4"/>
      </linearGradient>
    </defs>
    <path d="M660 240 H1200 V1200 H520 L450 1100 Z" fill="#ffffff" opacity="0.1"/>
    <path d="M900 680 H1200 V1200 H700 Z" fill="#ffffff" opacity="0.06"/>
    <path d="M0 1040 H520 L410 1200 H0 Z" fill="#ffffff" opacity="0.12"/>
    <path d="M0 960 H540 L470 1040 H0 Z" fill="#0b3f86" opacity="0.35"/>
    <path d="M0 100 H440 Q470 100 486 124 L712 470 Q722 490 710 510 L500 950 Q486 976 456 976 H0 Z"
          fill="none" stroke="#6aa8e0" stroke-width="6"/>
    <path role="img" aria-label="Photo of a technician in a hard hat repairing water pipes against a brick wall"
          d="M0 96 H440 Q466 96 480 118 L704 464 Q714 482 704 500 L496 948 Q484 972 456 972 H0 Z"
          fill="url(#photoTone)"/>
  </svg>

  <div class="brand-name">Brightwell Recovery</div>

  <h1 class="headline">Calm<br>Returns</h1>
  <div class="rule rule--headline"></div>

  <p class="intro">Brightwell Recovery, that reflects our commitment to building lasting relationships with our clients and providing top-quality restoration and cleaning services.</p>

  <h2 class="services-title">Our Services</h2>
  <div class="rule rule--services"></div>

  <ul class="service-list">
    <li><svg viewBox="0 0 24 24" fill="none" stroke="#fff" stroke-width="2" stroke-linecap="round" stroke-linejoin="round"><path d="M21 11v1a9 9 0 1 1-5.3-8.2"/><path d="M8 11.5l3.5 3.5L21 5"/></svg>Water Restoration</li>
    <li><svg viewBox="0 0 24 24" fill="none" stroke="#fff" stroke-width="2" stroke-linecap="round" stroke-linejoin="round"><path d="M21 11v1a9 9 0 1 1-5.3-8.2"/><path d="M8 11.5l3.5 3.5L21 5"/></svg>Emergency Flood Response</li>
    <li><svg viewBox="0 0 24 24" fill="none" stroke="#fff" stroke-width="2" stroke-linecap="round" stroke-linejoin="round"><path d="M21 11v1a9 9 0 1 1-5.3-8.2"/><path d="M8 11.5l3.5 3.5L21 5"/></svg>Mold Remediation</li>
    <li><svg viewBox="0 0 24 24" fill="none" stroke="#fff" stroke-width="2" stroke-linecap="round" stroke-linejoin="round"><path d="M21 11v1a9 9 0 1 1-5.3-8.2"/><path d="M8 11.5l3.5 3.5L21 5"/></svg>Trauma Scene Clean-up</li>
  </ul>

  <a class="cta" href="#">VIEW ALL</a>

  <div class="contact-phone">
    <svg viewBox="0 0 64 64" fill="none" stroke="#fff" stroke-width="5" stroke-linecap="round" stroke-linejoin="round">
      <path d="M12 6l10 2 4 14-7 5c3 8 9 14 17 17l5-7 14 4 2 10c-2 5-7 8-12 7C27 55 9 37 5 19 4 13 7 8 12 6z" fill="#fff" stroke="none"/>
      <path d="M38 14a14 14 0 0 1 12 12"/><path d="M40 4a24 24 0 0 1 20 20"/>
    </svg>
    <div>
      <div class="contact-label">Call Us</div>
      <div class="contact-number">(555) 014-2290</div>
    </div>
  </div>

  <div class="contact-web">
    <svg viewBox="0 0 24 24" fill="none" stroke="#fff" stroke-width="1.6">
      <circle cx="12" cy="12" r="10"/><ellipse cx="12" cy="12" rx="4.5" ry="10"/><path d="M2 12h20M4 6.5h16M4 17.5h16"/>
    </svg>
    <span>www.brightwellrecovery.example</span>
  </div>
</body>
</html>
```